Real Estate Website

Please design a real estate website

The menu needs to be :
Home
About us
Houses for sale
Land for sale
Sold properties
Holiday accommodation
Rentals
Consumer affairs
Contact us.

Contact details to show in the footer:
Pinecrest Real Estate
27 Hollowmere Drive
Kelpmoor Bay 3962
03 5290 7741

Please add a 'contact us' form in the footer like on https://www.quillbrookestate.com.au/

Design of site should be a photo/slideshow please make it a lifestyle shot and use a photo from a google image search of 'golden beach victoria australia' as a placeholder.

Under this needs to be a section for a heading and description with about us button.

Further under this should be 6 feature properties like https://www.marlowvaleproperty.com.au/ and then under that a 'book a free appraisal' banner like the one on https://www.marlowvaleproperty.com.au/

Attached is the business logo

```html
<!DOCTYPE html>
<html lang="en">
<head>
<meta charset="utf-8">
<title>Sandhaven Real Estate</title>
<link href="https://fonts.googleapis.com/css2?family=Oswald:wght@600;700&family=Lato:wght@400;700&display=swap" rel="stylesheet">
<style>
:root{
  --blue:#0d4a9a;
  --red:#c9202f;
  --tan:#c5a66f;
  --ink:#1c1c1c;
  --text:#444;
  --rule:#d9d9d9;
  --white:#fff;
}
*{box-sizing:border-box;margin:0;padding:0}
html,body{width:1200px;height:3136px;overflow:hidden;background:var(--white)}
body{position:relative;font-family:'Lato',sans-serif;color:var(--text)}
.abs{position:absolute}
.heading{font-family:'Oswald',sans-serif;font-weight:700;color:var(--ink);text-transform:uppercase;letter-spacing:.2px}
.btn{position:absolute;display:flex;align-items:center;justify-content:center;background:var(--blue);color:var(--white);border-radius:22px;font-size:13px;text-transform:uppercase}

/* hero */
.hero{left:0;top:0;width:1200px;height:735px;background:linear-gradient(180deg,#5b6f88 0%,#8a9db4 22%,#6f8492 38%,#4f6a72 55%,#6b6650 75%,#3e3f36 100%)}
.hero-top{left:0;top:0;width:1200px;height:160px;background:linear-gradient(180deg,rgba(25,40,70,.55),rgba(25,40,70,0))}
.phone{left:117px;top:49px;display:flex;align-items:center;gap:8px;color:var(--white);font-size:12px}
.ico-circle{width:26px;height:26px;border-radius:50%;background:var(--tan);display:flex;align-items:center;justify-content:center}
.brand-top{left:460px;top:56px;width:284px;text-align:center;color:var(--white);font-weight:700;font-size:17px;line-height:1.15;letter-spacing:.5px}
.social{display:flex;gap:14px}
.social span{width:24px;height:24px;border-radius:50%;background:var(--tan);display:block}
.nav{left:0;top:118px;width:1200px;display:flex;justify-content:center;gap:40px;color:var(--white);font-size:12.5px}
.nav a{color:inherit;text-decoration:none;position:relative;padding-bottom:13px}
.nav a.active::after{content:"";position:absolute;left:-2px;right:-2px;bottom:-10px;height:3px;background:var(--red)}
.nav-rule{left:0;top:156px;width:1200px;height:1px;background:rgba(255,255,255,.55)}
.hero-kicker{left:0;top:290px;width:1200px;text-align:center;font-size:44px}
.hero-title{left:0;top:345px;width:1200px;text-align:center;font-size:70px}
.hero-copy{left:350px;top:452px;width:500px;text-align:center;color:var(--white);font-size:12px;line-height:22px}
.dots{left:578px;top:671px;display:flex;gap:7px}
.dots i{width:10px;height:10px;border-radius:50%;background:var(--white);display:block}
.dots i.on{background:var(--red);box-shadow:0 0 0 2px var(--white)}

/* about */
.about-photo{left:643px;top:688px;width:557px;height:410px;background:var(--white)}
.about-photo div{position:absolute;left:7px;top:7px;right:0;bottom:7px;background:linear-gradient(160deg,#e4e7ec 0%,#cdd2d6 35%,#9aa49a 60%,#555f52 100%)}
.about-small{left:476px;top:864px;width:322px;height:195px;background:var(--white)}
.about-small div{position:absolute;left:7px;top:7px;right:7px;bottom:7px;background:linear-gradient(135deg,#eceae6 0%,#d9d5cd 50%,#b99c77 100%)}
.about-title{left:113px;top:826px;font-size:26px}
.about-copy{left:113px;top:888px;width:335px;font-size:11.5px;line-height:18px}

/* listings */
.listings-title{left:0;top:1230px;width:1200px;text-align:center;font-size:26px}
.card{position:absolute;width:314px;height:444px;background:var(--white);border-radius:6px;box-shadow:0 2px 14px rgba(0,0,0,.09);overflow:hidden}
.card-photo{height:253px;position:relative}
.tag{position:absolute;left:11px;top:16px;background:var(--red);color:var(--white);font-family:'Oswald',sans-serif;font-weight:600;font-size:12.5px;padding:3px 11px;border-radius:13px}
.card-body{padding:18px 26px 0}
.card-head{display:flex;justify-content:space-between;align-items:center}
.card-name{font-family:'Oswald',sans-serif;font-weight:600;font-size:12.5px;color:var(--ink)}
.card-price{font-family:'Oswald',sans-serif;font-weight:700;font-size:17px;color:var(--red)}
.specs{display:flex;gap:14px;margin-top:22px;font-size:12.5px;color:#555;padding-left:6px}
.specs span{display:flex;align-items:center;gap:8px}
.card-rule{height:1px;background:var(--rule);margin:26px 0 0}
.card-foot{display:flex;justify-content:space-between;align-items:center;margin-top:22px}
.addr{display:flex;gap:9px;font-size:12.5px;line-height:16px;color:#444;padding-left:4px}
.view{width:82px;height:34px;border-radius:17px;background:var(--blue);color:var(--white);font-size:12px;display:flex;align-items:center;justify-content:center}

/* appraisal */
.sell-band{left:0;top:2441px;width:1200px;height:252px;background:linear-gradient(90deg,#c9202f 0%,#cf3a48 45%,#e49aa0 70%,#eeeeee 100%)}
.sell-house{left:675px;top:2300px;width:525px;height:393px;background:linear-gradient(180deg,#d8d3c7 0%,#8c8674 45%,#6f6a57 70%,#3d5a35 100%);clip-path:polygon(30% 0,100% 28%,100% 100%,0 100%,0 55%)}
.sell-title{left:112px;top:2482px;font-size:25px;line-height:32px}
.sell-copy{left:113px;top:2560px;width:540px;color:var(--white);font-size:12px;line-height:19px}

/* footer */
.foot-mark{left:130px;top:2812px;width:48px;height:48px;border-radius:50%;background:var(--blue)}
.brand-foot{left:110px;top:2876px;width:200px;color:var(--blue);font-weight:700;font-size:19px;line-height:1.2;white-space:nowrap}
.foot-social{left:135px;top:2995px}
.col-title{font-size:18px}
.links{list-style:none;font-size:11.5px;line-height:17.9px;color:#444}
.info{font-size:11.5px;line-height:18px;color:#444}
.info-row{display:flex;gap:14px;position:absolute;left:548px}
.form-box{left:792px;top:2739px;width:298px;height:397px;background:var(--tan);border-bottom:6px solid var(--white)}
.form-title{position:absolute;left:0;top:18px;width:100%;text-align:center;font-size:26px}
.field{position:absolute;left:31px;width:229px}
.field label{display:block;color:var(--white);font-size:10.5px;font-style:italic;margin-bottom:2px}
.field div{background:var(--white);height:35px}
.send{position:absolute;left:31px;top:315px;width:229px;height:38px;border-radius:19px;background:var(--blue);color:var(--white);font-size:12px;display:flex;align-items:center;justify-content:center}
.copy-bar{left:0;top:3093px;width:1200px;height:43px;background:var(--blue)}
.copyright{left:114px;top:3112px;color:var(--white);font-size:11.5px}
</style>
</head>
<body>

<!-- hero -->
<div class="abs hero" role="img" aria-label="Lifestyle photo of a rugged coastline with limestone sea stacks, cliffs and a sandy beach"></div>
<div class="abs hero-top"></div>
<div class="abs phone">
  <span class="ico-circle"><svg width="13" height="13" viewBox="0 0 24 24"><path fill="#fff" d="M6.6 10.8a15.5 15.5 0 0 0 6.6 6.6l2.2-2.2c.3-.3.7-.4 1-.2 1.1.4 2.3.6 3.6.6.6 0 1 .4 1 1V20c0 .6-.4 1-1 1A17 17 0 0 1 3 4c0-.6.4-1 1-1h3.5c.6 0 1 .4 1 1 0 1.3.2 2.5.6 3.6.1.3 0 .7-.2 1z"/></svg></span>
  03 5290 7741
</div>
<div class="abs brand-top">SANDHAVEN<br>REAL ESTATE PTY LTD</div>
<div class="abs social" style="left:952px;top:57px"><span></span><span></span><span></span><span></span></div>
<nav class="abs nav">
  <a class="active">Home</a><a>About us</a><a>Houses for sale</a><a>Land for sale</a><a>Sold properties</a><a>Holiday accommodation</a><a>Rentals</a><a>Consumer affairs</a><a>Contact us</a>
</nav>
<div class="abs nav-rule"></div>
<div class="abs heading hero-kicker" style="color:#fff">Improve life means</div>
<div class="abs heading hero-title" style="color:#fff">Beautiful home</div>
<p class="abs hero-copy">Lorem Ipsum is simply dummy text of the printing and typesetting industry. Lorem Ipsum has been the industry's standard dummy text ever since the 1500s.</p>
<div class="btn" style="left:529px;top:517px;width:154px;height:40px">View&nbsp; Listing</div>
<div class="abs dots"><i class="on"></i><i></i><i></i></div>

<!-- about -->
<div class="abs about-photo"><div role="img" aria-label="Modern white house with timber shutters beside a leafy tree"></div></div>
<div class="abs about-small"><div role="img" aria-label="Bright bedroom with a large window and timber furniture"></div></div>
<h2 class="abs heading about-title">About us</h2>
<p class="abs about-copy">Lorem Ipsum is simply dummy text of the printing and typesetting industry. Lorem Ipsum has been the industry's standard dummy text ever since the 1500s, when an unknown printer took a galley of type and scrambled it to make a type specimen book. It has survived not only five centuries, but also the leap into electronic typesetting, remaining essentially unchanged.</p>
<div class="btn" style="left:113px;top:1049px;width:152px;height:42px">Read more</div>

<!-- listings -->
<h2 class="abs heading listings-title">Featured listings</h2>

<svg width="0" height="0" style="position:absolute">
  <defs>
    <symbol id="i-bed" viewBox="0 0 20 14"><path fill="#c5a66f" d="M2 1h16v5H2zM0 7h20v5h-2v2h-2v-2H4v2H2v-2H0z"/></symbol>
    <symbol id="i-bath" viewBox="0 0 20 18"><path fill="#c5a66f" d="M3 1h5v2H5v5h15v3a5 5 0 0 1-4 5l1 2h-2l-1-2H6l-1 2H3l1-2a5 5 0 0 1-4-5V8h3z"/></symbol>
    <symbol id="i-area" viewBox="0 0 18 18"><path fill="none" stroke="#c5a66f" stroke-width="1.6" d="M1 1l16 16M17 1L1 17M1 6V1h5M12 1h5v5M17 12v5h-5M6 17H1v-5"/></symbol>
    <symbol id="i-pin" viewBox="0 0 12 16"><path fill="#c9202f" d="M6 0a6 6 0 0 0-6 6c0 4.5 6 10 6 10s6-5.5 6-10a6 6 0 0 0-6-6zm0 8.5A2.5 2.5 0 1 1 6 3.5a2.5 2.5 0 0 1 0 5z"/></symbol>
  </defs>
</svg>

<article class="card" style="left:114px;top:1318px">
  <div class="card-photo" role="img" aria-label="Bedroom with ocean view window" style="background:linear-gradient(135deg,#e9e7e2,#c9c4ba 60%,#8d8372)"><span class="tag">FOR RENT</span></div>
  <div class="card-body">
    <div class="card-head"><span class="card-name">PROPERTY NAME #01</span><span class="card-price">$7000</span></div>
    <div class="specs"><span><svg width="18" height="13"><use href="#i-bed"/></svg>4 Beds</span><span><svg width="17" height="15"><use href="#i-bath"/></svg>2 Bath</span><span><svg width="15" height="15"><use href="#i-area"/></svg>720 sqft</span></div>
    <div class="card-rule"></div>
    <div class="card-foot"><div class="addr"><svg width="11" height="15"><use href="#i-pin"/></svg><span>937 Augusta Drive Mc<br>Lean, VA 22101</span></div><div class="view">VIEW</div></div>
  </div>
</article>
<article class="card" style="left:443px;top:1318px">
  <div class="card-photo" role="img" aria-label="Large white two-storey house with verandas and a pool" style="background:linear-gradient(180deg,#3c69b8,#9fb4d4 45%,#e8e8e6 70%,#8d6e5a)"><span class="tag">FOR SALE</span></div>
  <div class="card-body">
    <div class="card-head"><span class="card-name">PROPERTY NAME #02</span><span class="card-price">$25000</span></div>
    <div class="specs"><span><svg width="18" height="13"><use href="#i-bed"/></svg>5 Beds</span><span><svg width="17" height="15"><use href="#i-bath"/></svg>3 Bath</span><span><svg width="15" height="15"><use href="#i-area"/></svg>800 sqft</span></div>
    <div class="card-rule"></div>
    <div class="card-foot"><div class="addr"><svg width="11" height="15"><use href="#i-pin"/></svg><span>7495 Foster St.<br>Fullerton, CA 92831</span></div><div class="view">VIEW</div></div>
  </div>
</article>
<article class="card" style="left:773px;top:1318px">
  <div class="card-photo" role="img" aria-label="Grey living room with sofas and arched windows" style="background:linear-gradient(180deg,#dcdcdc,#b9b9b7 55%,#8b8c89)"><span class="tag">FOR RENT</span></div>
  <div class="card-body">
    <div class="card-head"><span class="card-name">PROPERTY NAME #03</span><span class="card-price">$8000</span></div>
    <div class="specs"><span><svg width="18" height="13"><use href="#i-bed"/></svg>2 Beds</span><span><svg width="17" height="15"><use href="#i-bath"/></svg>2 Bath</span><span><svg width="15" height="15"><use href="#i-area"/></svg>550 sqft</span></div>
    <div class="card-rule"></div>
    <div class="card-foot"><div class="addr"><svg width="11" height="15"><use href="#i-pin"/></svg><span>77 Bradford Ave.<br>Dubuque, IA 52001</span></div><div class="view">VIEW</div></div>
  </div>
</article>

<article class="card" style="left:114px;top:1786px">
  <div class="card-photo" role="img" aria-label="Modern dark and white multi-level house" style="background:linear-gradient(160deg,#4a7fc2,#a8c0dc 40%,#3a3f48 75%,#6b6f74)"><span class="tag">FOR SALE</span></div>
  <div class="card-body">
    <div class="card-head"><span class="card-name">PROPERTY NAME #04</span><span class="card-price">$35000</span></div>
    <div class="specs"><span><svg width="18" height="13"><use href="#i-bed"/></svg>4 Beds</span><span><svg width="17" height="15"><use href="#i-bath"/></svg>4 Bath</span><span><svg width="15" height="15"><use href="#i-area"/></svg>1000 sqft</span></div>
    <div class="card-rule"></div>
    <div class="card-foot"><div class="addr"><svg width="11" height="15"><use href="#i-pin"/></svg><span>201 Beaver Ridge Dr.<br>Kokomo, IN 46901</span></div><div class="view">VIEW</div></div>
  </div>
</article>
<article class="card" style="left:443px;top:1786px">
  <div class="card-photo" role="img" aria-label="Open dining and living room with marble table and pendant lights" style="background:linear-gradient(180deg,#6d6a66,#9a948c 45%,#7b6a58 80%,#55504a)"><span class="tag">FOR SALE</span></div>
  <div class="card-body">
    <div class="card-head"><span class="card-name">PROPERTY NAME #05</span><span class="card-price">$25000</span></div>
    <div class="specs"><span><svg width="18" height="13"><use href="#i-bed"/></svg>2 Beds</span><span><svg width="17" height="15"><use href="#i-bath"/></svg>2 Bath</span><span><svg width="15" height="15"><use href="#i-area"/></svg>720 sqft</span></div>
    <div class="card-rule"></div>
    <div class="card-foot"><div class="addr"><svg width="11" height="15"><use href="#i-pin"/></svg><span>7971 Applegate Ave.<br>Corona, NY 11368</span></div><div class="view">VIEW</div></div>
  </div>
</article>
<article class="card" style="left:773px;top:1786px">
  <div class="card-photo" role="img" aria-label="Minimal living room with sofa and sheer curtains" style="background:linear-gradient(180deg,#d8d6d2,#b8b0a6 50%,#a09586)"><span class="tag">FOR RENT</span></div>
  <div class="card-body">
    <div class="card-head"><span class="card-name">PROPERTY NAME #06</span><span class="card-price">$9000</span></div>
    <div class="specs"><span><svg width="18" height="13"><use href="#i-bed"/></svg>4 Beds</span><span><svg width="17" height="15"><use href="#i-bath"/></svg>2 Bath</span><span><svg width="15" height="15"><use href="#i-area"/></svg>720 sqft</span></div>
    <div class="card-rule"></div>
    <div class="card-foot"><div class="addr"><svg width="11" height="15"><use href="#i-pin"/></svg><span>7074 Wall St.<br>Fairfax, VA 22030</span></div><div class="view">VIEW</div></div>
  </div>
</article>

<div class="btn" style="left:521px;top:2293px;width:162px;height:41px">View more listing</div>

<!-- appraisal banner -->
<div class="abs sell-band"></div>
<div class="abs sell-house" role="img" aria-label="Two-storey weatherboard house with red windows, front porch and a tree"></div>
<h2 class="abs heading sell-title" style="color:#fff">Sell your property with<br>Sandhaven Real Estate PTY LTD</h2>
<p class="abs sell-copy">Lorem Ipsum is simply dummy text of the printing and typesetting industry. Lorem Ipsum has been the industry's standard dummy text ever since the 1500s,.</p>
<div class="btn" style="left:114px;top:2613px;width:183px;height:41px">Book a free appraisal</div>

<!-- footer -->
<div class="abs foot-mark"></div>
<div class="abs brand-foot">SANDHAVEN<br>REAL ESTATE PTY LTD</div>
<div class="abs social foot-social"><span></span><span></span><span></span><span></span></div>

<h3 class="abs heading col-title" style="left:368px;top:2816px">Quick links</h3>
<ul class="abs links" style="left:368px;top:2895px">
  <li>Home</li><li>About us</li><li>Houses for sale</li><li>Land for sale</li><li>Sold properties</li><li>Holiday accommodation</li><li>Rentals</li><li>Consumer affairs</li><li>Contact us</li>
</ul>

<h3 class="abs heading col-title" style="left:548px;top:2816px">Contact info..</h3>
<div class="info-row info" style="top:2895px">
  <svg width="14" height="16" viewBox="0 0 12 16"><path fill="none" stroke="#c5a66f" stroke-width="1.2" d="M6 1a5 5 0 0 0-5 5c0 4 5 9 5 9s5-5 5-9a5 5 0 0 0-5-5z"/><circle cx="6" cy="6" r="1.8" fill="none" stroke="#c5a66f" stroke-width="1.2"/></svg>
  <span>Pinecrest Real Estate<br>27 Hollowmere Drive<br>Kelpmoor Bay 3962</span>
</div>
<div class="info-row info" style="top:2968px">
  <svg width="15" height="15" viewBox="0 0 24 24"><path fill="none" stroke="#c5a66f" stroke-width="1.6" d="M6.6 10.8a15.5 15.5 0 0 0 6.6 6.6l2.2-2.2c.3-.3.7-.4 1-.2 1.1.4 2.3.6 3.6.6.6 0 1 .4 1 1V20c0 .6-.4 1-1 1A17 17 0 0 1 3 4c0-.6.4-1 1-1h3.5c.6 0 1 .4 1 1 0 1.3.2 2.5.6 3.6.1.3 0 .7-.2 1z"/></svg>
  <span>03 5290 7741</span>
</div>
<div class="info-row info" style="top:3004px">
  <svg width="15" height="13" viewBox="0 0 16 12"><rect x="1" y="1" width="14" height="10" fill="none" stroke="#c5a66f" stroke-width="1.2"/><path d="M1 1l7 6 7-6" fill="none" stroke="#c5a66f" stroke-width="1.2"/></svg>
  <span>info@sandhavenrealestate.com</span>
</div>

<div class="copy-bar abs"></div>
<p class="abs copyright">© 2021 Sandhaven Real Estate PTY LTD – All Rights Reserved</p>

<form class="abs form-box">
  <h3 class="heading form-title" style="color:#fff">Contact us</h3>
  <div class="field" style="top:64px"><label>Full Name*</label><div></div></div>
  <div class="field" style="top:114px"><label>Phone*</label><div></div></div>
  <div class="field" style="top:167px"><label>Email Address*</label><div></div></div>
  <div class="field" style="top:220px"><label>Message*</label><div style="height:72px"></div></div>
  <div class="send">SEND NOW</div>
</form>

</body>
</html>
```